Design Cloud for Core Values & Attributes

See Image Example Below "Word Cloud" this is what we would like this to look like.
The second image is all of the Core Value and Attributes I will list below.
CORE VALUES need to be the bigger words (based off the image I sent) Capitalized, BOLD, Navy
Independence, Capitalism, Trust, Fun, Safety, Growth
ATTRIBUTES need to be the smaller words, lower case, non-bold, lighter blue mixed in (based off the image I sent):
Humility, Consistency, Open Mindedness, Curiosity, Selflessness, Caring, Conscientiousness, Honorable, Cunning, Competitive, Compartmentalization, Innovative, Perseverance, Authenticity, Decisiveness, Self-efficacy, Accountability, Generosity, Humor, Optimism, Resilience, Inclusive, Insouciance to what others think, Courage, Decisive, Curious, Integrity

```html
<!DOCTYPE html>
<html lang="en">
<head>
<meta charset="utf-8">
<title>Core Values Word Cloud</title>
<link rel="stylesheet" href="https://fonts.googleapis.com/css2?family=Saira:wght@800&family=Roboto+Condensed:wght@700&family=Open+Sans:wght@600;700&family=Questrial&display=swap">
<style>
  :root{
    --stage:#8493a9;
    --navy:#0a1196;
    --royal:#0a4fb5;
    --deep:#1e5bc6;
    --bright:#2f7ae8;
    --mid:#3f7fe0;
    --sky:#5a9ae8;
    --pale:#7fa8e0;
    --mist:#a8c0ea;
    --slate:#5a7fb8;
    --corner-strong:#2f6fd8;
    --corner-soft:#7fb0ee;
  }
  html,body{margin:0;padding:0;width:1200px;height:1200px;overflow:hidden;background:var(--stage)}
  .poster{position:absolute;left:0;top:137px;width:1200px;height:925px;display:block}
  .paper{fill:url(#paperWash)}
  .corner-accent-tl{fill:url(#cornerWashTL)}
  .corner-accent-br{fill:url(#cornerWashBR)}
  .value{font-family:"Saira",sans-serif;font-weight:800;fill:var(--navy)}
  .pillar{font-family:"Roboto Condensed",sans-serif;font-weight:700;fill:var(--royal)}
  .attr{font-family:"Open Sans",sans-serif;font-weight:700}
  .attr-geo{font-family:"Questrial",sans-serif;font-weight:400;stroke-width:2.2;paint-order:stroke}
  .c-deep{fill:var(--deep)} .c-bright{fill:var(--bright)} .c-mid{fill:var(--mid)}
  .c-sky{fill:var(--sky)} .c-pale{fill:var(--pale)} .c-mist{fill:var(--mist)} .c-slate{fill:var(--slate)}
  .attr-geo.c-pale{stroke:var(--pale)} .attr-geo.c-slate{stroke:var(--slate)} .attr-geo.c-mist{stroke:var(--mist)}
</style>
</head>
<body>
<svg class="poster" viewBox="0 0 1678 1294" xmlns="http://www.w3.org/2000/svg" role="img" aria-label="Core Values word cloud">
  <defs>
    <linearGradient id="paperWash" x1="0" y1="0" x2="1" y2="1">
      <stop offset="0" stop-color="#fbfbff"/>
      <stop offset="0.5" stop-color="#eef0fc"/>
      <stop offset="1" stop-color="#e6eafb"/>
    </linearGradient>
    <linearGradient id="cornerWashTL" x1="0" y1="0" x2="1" y2="1">
      <stop offset="0" stop-color="var(--corner-strong)" stop-opacity="0.9"/>
      <stop offset="0.45" stop-color="var(--corner-soft)" stop-opacity="0.55"/>
      <stop offset="1" stop-color="var(--corner-soft)" stop-opacity="0"/>
    </linearGradient>
    <linearGradient id="cornerWashBR" x1="1" y1="1" x2="0" y2="0">
      <stop offset="0" stop-color="var(--corner-strong)" stop-opacity="0.9"/>
      <stop offset="0.45" stop-color="var(--corner-soft)" stop-opacity="0.55"/>
      <stop offset="1" stop-color="var(--corner-soft)" stop-opacity="0"/>
    </linearGradient>
  </defs>

  <rect class="paper" width="1678" height="1294" role="img" aria-label="Soft lavender diamond background"/>

  <rect class="corner-accent-tl" x="0" y="0" width="265" height="303" role="img" aria-label="Cluster of blue squares in the top left corner"/>
  <rect class="corner-accent-br" x="1397" y="993" width="281" height="301" role="img" aria-label="Cluster of blue squares in the bottom right corner"/>

  <g class="headline">
    <text class="value" x="571" y="558" font-size="190" textLength="545" lengthAdjust="spacingAndGlyphs">CORE</text>
    <text class="value" x="440" y="723" font-size="200" textLength="808" lengthAdjust="spacingAndGlyphs">VALUES</text>
  </g>

  <g class="pillars">
    <text class="pillar" x="383" y="568" font-size="150" textLength="178" lengthAdjust="spacingAndGlyphs">FUN</text>
    <text class="pillar" x="360" y="820" font-size="108" textLength="521" lengthAdjust="spacingAndGlyphs">INDEPENDENCE</text>
    <text class="pillar" x="1013" y="810" font-size="102" textLength="375" lengthAdjust="spacingAndGlyphs">CAPITALISM</text>
    <text class="pillar" transform="translate(561 446) rotate(-90)" font-size="128" textLength="283" lengthAdjust="spacingAndGlyphs">SAFETY</text>
    <text class="pillar" transform="translate(1235 570) rotate(-90)" font-size="126" textLength="240" lengthAdjust="spacingAndGlyphs">TRUST</text>
    <text class="pillar" transform="translate(991 1053) rotate(-90)" font-size="128" textLength="315" lengthAdjust="spacingAndGlyphs">GROWTH</text>
  </g>

  <g class="attributes">
    <text class="attr c-mid" x="581" y="285" font-size="52" textLength="204" lengthAdjust="spacingAndGlyphs">CURIOUS</text>
    <text class="attr-geo c-pale" x="583" y="326" font-size="46" textLength="205" lengthAdjust="spacingAndGlyphs">COURAGE</text>
    <text class="attr c-slate" x="848" y="260" font-size="40" textLength="195" lengthAdjust="spacingAndGlyphs">INTEGRITY</text>
    <text class="attr c-sky" x="803" y="326" font-size="74" textLength="305" lengthAdjust="spacingAndGlyphs">HUMILITY</text>
    <text class="attr c-sky" x="1143" y="274" font-size="34" textLength="335" lengthAdjust="spacingAndGlyphs">CONSCIENTIOUSNESS</text>
    <text class="attr c-bright" x="1138" y="315" font-size="46" textLength="292" lengthAdjust="spacingAndGlyphs">CONSISTENCY</text>
    <text class="attr-geo c-slate" x="581" y="391" font-size="68" textLength="525" lengthAdjust="spacingAndGlyphs">ACCOUNTABILITY</text>
    <text class="attr c-pale" x="235" y="386" font-size="42" textLength="216" lengthAdjust="spacingAndGlyphs">RESILIENCE</text>
    <text class="attr c-deep" x="176" y="451" font-size="64" textLength="275" lengthAdjust="spacingAndGlyphs">HUMILITY</text>
    <text class="attr c-slate" x="148" y="493" font-size="34" textLength="217" lengthAdjust="spacingAndGlyphs">INSOUCIANCE</text>
    <text class="attr c-slate" x="107" y="524" font-size="34" textLength="258" lengthAdjust="spacingAndGlyphs">TO WHAT OTHERS</text>
    <text class="attr c-bright" x="218" y="573" font-size="44" textLength="150" lengthAdjust="spacingAndGlyphs">HUMOR</text>
    <text class="attr c-pale" x="99" y="630" font-size="76" textLength="324" lengthAdjust="spacingAndGlyphs">OPTIMISM</text>
    <text class="attr c-slate" x="343" y="673" font-size="34" textLength="92" lengthAdjust="spacingAndGlyphs">THINK</text>
    <text class="attr c-bright" x="220" y="721" font-size="52" textLength="235" lengthAdjust="spacingAndGlyphs">CURIOSITY</text>
    <text class="attr c-deep" x="188" y="770" font-size="36" textLength="155" lengthAdjust="spacingAndGlyphs">CUNNING</text>
    <text class="attr c-sky" x="95" y="816" font-size="40" textLength="248" lengthAdjust="spacingAndGlyphs">DECISIVENESS</text>
    <text class="attr c-pale" x="166" y="883" font-size="72" textLength="294" lengthAdjust="spacingAndGlyphs">HUMILITY</text>
    <text class="attr c-bright" x="211" y="925" font-size="38" textLength="237" lengthAdjust="spacingAndGlyphs">SELFLESSNESS</text>

    <text class="attr c-slate" x="585" y="870" font-size="50" textLength="250" lengthAdjust="spacingAndGlyphs">GENEROSITY</text>
    <text class="attr c-pale" x="691" y="905" font-size="40" textLength="142" lengthAdjust="spacingAndGlyphs">CARING</text>
    <text class="attr c-bright" x="568" y="944" font-size="42" textLength="265" lengthAdjust="spacingAndGlyphs">PERSEVERANCE</text>
    <text class="attr c-pale" x="581" y="991" font-size="46" textLength="250" lengthAdjust="spacingAndGlyphs">HONORABLE</text>

    <text class="attr c-mid" x="1016" y="861" font-size="66" textLength="341" lengthAdjust="spacingAndGlyphs">HONORABLE</text>
    <text class="attr c-slate" x="1058" y="902" font-size="36" textLength="393" lengthAdjust="spacingAndGlyphs">COMPARTMENTALIZATION</text>
    <text class="attr c-pale" x="1060" y="938" font-size="38" textLength="335" lengthAdjust="spacingAndGlyphs">CONSCIENTIOUSNESS</text>
    <text class="attr c-mid" x="1060" y="978" font-size="38" textLength="241" lengthAdjust="spacingAndGlyphs">PERSEVERANCE</text>
    <text class="attr c-deep" x="1060" y="1014" font-size="38" textLength="198" lengthAdjust="spacingAndGlyphs">INNOVATIVE</text>
    <text class="attr-geo c-pale" x="1058" y="1058" font-size="52" textLength="295" lengthAdjust="spacingAndGlyphs">COMPETITIVE</text>
    <text class="attr c-bright" x="898" y="1096" font-size="40" textLength="315" lengthAdjust="spacingAndGlyphs">ACCOUNTABILITY</text>
    <text class="attr c-pale" x="898" y="1132" font-size="40" textLength="215" lengthAdjust="spacingAndGlyphs">INNOVATIVE</text>

    <text class="attr c-deep" x="1296" y="643" font-size="30" textLength="134" lengthAdjust="spacingAndGlyphs">CURIOSITY</text>
    <text class="attr c-sky" x="1298" y="683" font-size="42" textLength="165" lengthAdjust="spacingAndGlyphs">HUMILITY</text>
    <text class="attr c-mid" x="1298" y="721" font-size="50" textLength="178" lengthAdjust="spacingAndGlyphs">CARING</text>

    <text class="attr-geo c-slate" transform="translate(416 340) rotate(-90)" font-size="44" textLength="160" lengthAdjust="spacingAndGlyphs">CARING</text>
    <text class="attr c-bright" transform="translate(455 340) rotate(-90)" font-size="40" textLength="204" lengthAdjust="spacingAndGlyphs">INCLUSIVE</text>
    <text class="attr-geo c-slate" transform="translate(786 238) rotate(-90)" font-size="44" textLength="160" lengthAdjust="spacingAndGlyphs">CARING</text>
    <text class="attr-geo c-mist" transform="translate(838 266) rotate(-90)" font-size="46" textLength="190" lengthAdjust="spacingAndGlyphs">DECISIVE</text>
    <text class="attr-geo c-pale" transform="translate(1285 718) rotate(-90)" font-size="42" textLength="385" lengthAdjust="spacingAndGlyphs">OPEN MINDEDNESS</text>
    <text class="attr c-slate" transform="translate(1333 608) rotate(-90)" font-size="42" textLength="275" lengthAdjust="spacingAndGlyphs">SELFLESSNESS</text>
    <text class="attr c-pale" transform="translate(498 1103) rotate(-90)" font-size="40" textLength="265" lengthAdjust="spacingAndGlyphs">SELF-EFFICACY</text>
    <text class="attr c-slate" transform="translate(553 1193) rotate(-90)" font-size="56" textLength="360" lengthAdjust="spacingAndGlyphs">AUTHENTICITY</text>
    <text class="attr c-bright" transform="translate(888 1128) rotate(-90)" font-size="64" textLength="295" lengthAdjust="spacingAndGlyphs">CURIOSITY</text>
    <text class="attr c-sky" transform="translate(1048 1053) rotate(-90)" font-size="40" textLength="175" lengthAdjust="spacingAndGlyphs">CUNNING</text>
  </g>
</svg>
</body>
</html>
```